Website for The Copper Lantern

We need an impressive e-commerce website for our newly launched business "The Copper Lantern".
The Copper Lantern searches store-front and online retailers for diamond engagement rings according to the client's specified requirements. We want to save people time by doing the shopping around for them.
We can relate to, and we love, www.roomtrellis.com
Like roomtrellis.com, we want to offer website visitors a quick run-down on how the process works, then offer them to elect a service package and pay for that package on the spot.
Content pages:
HOME
HOW IT WORKS
DIAMOND GALLERY
ABOUT
FAQs
CONTACT
Inclusions: Our logo and Facebook and Instagram buttons
We want to be able to easily edit this website, We want it to display well on iPhone and android, We want it to be clean and striking.
Like our logo, we want our website to embody elegant masculinity.
Target Market(s)
Men in market for diamond ring purchase $5k - $50k
Industry/Entity Type
Business
Number of Pages Required
5+ page
Font styles to use
Look and feel

```html
<!DOCTYPE html>
<html lang="en">
<head>
<meta charset="utf-8">
<title>The Copper Lantern</title>
<link href="https://fonts.googleapis.com/css2?family=Roboto:wght@300;400&family=Open+Sans:wght@400;600&family=Noto+Serif&display=swap" rel="stylesheet">
<style>
:root{
  --ink:#333;
  --text:#555;
  --muted:#888;
  --line:#dcdcdc;
  --btn:#5b5b5b;
  --paper:#fff;
  --mist:#f2f2f2;
  --footer:#5e5e5e;
}
*{margin:0;padding:0;box-sizing:border-box}
html,body{width:682px;height:1200px;overflow:hidden;background:var(--paper)}
body{position:relative;font-family:"Open Sans",sans-serif;color:var(--text)}
.abs{position:absolute}
.center{text-align:center}
.heading{font-family:"Roboto",sans-serif;font-weight:300;color:var(--ink)}
.rule{position:absolute;width:20px;height:1px;background:var(--ink)}
.btn{position:absolute;background:var(--btn);color:#fff;font-size:7.5px;display:flex;align-items:center;justify-content:center;border-radius:1px}
.btn-outline{position:absolute;border:1px solid var(--muted);background:#fff;color:var(--ink);font-size:7px;display:flex;align-items:center;justify-content:center}

/* header */
.brand{left:40px;top:22px;width:70px;font-family:"Roboto",sans-serif;font-size:8px;color:var(--ink);text-align:center;line-height:1.2;display:flex;flex-direction:column;align-items:center;gap:3px}
.brand-mark{width:14px;height:14px;border:1px solid var(--muted);border-radius:50%}
.nav{top:16px;font-size:7.5px;color:var(--ink)}
.hero{left:0;top:0;width:682px;height:348px;background:radial-gradient(ellipse at 70% 40%,#d8d8d8 0%,#ececec 35%,#fafafa 75%);border-bottom:1px solid var(--line)}
.hero-kicker{left:0;width:682px;top:137px;font-size:22px}
.hero-title{left:0;width:682px;top:162px;font-size:33px;font-weight:300}
.hero-line{left:177px;width:332px;height:1px;background:#bbb}
.hero-sub{left:0;width:682px;top:211px;font-size:7.5px;color:var(--ink);letter-spacing:.1px}

/* experience */
.exp-bg{left:0;top:350px;width:682px;height:218px;background:linear-gradient(90deg,#ececec 0%,#f7f7f7 40%,#fff 60%)}
.photo-ring{left:0;top:450px;width:320px;height:118px;background:linear-gradient(180deg,rgba(235,235,235,0) 0%,#e4e4e4 70%,#ddd 100%)}
.step{width:146px;margin-left:-73px;top:408px}
.step-icon{width:59px;height:59px;margin:0 auto;border:1px dashed #555;border-radius:50%;display:flex;align-items:center;justify-content:center}
.step h3{font-size:8px;font-weight:400;color:var(--ink);margin-top:14px}
.step p{font-size:7px;line-height:11px;margin-top:3px;color:var(--text)}

/* packages */
.pkg-photo{left:600px;top:680px;width:82px;height:108px;background:linear-gradient(160deg,#fff 0%,#e6e6e6 60%,#cfc7bd 100%)}
.pkg{top:624px;width:194px;height:134px;border:1px solid var(--line);background:#fff}
.pkg .from,.pkg .price,.pkg .unit{position:absolute;left:0;width:100%;display:block;text-align:center}
.pkg .from{top:20px;font-size:7.5px;color:var(--muted)}
.pkg .price{top:31px;font-size:18px;font-weight:600;color:var(--text);line-height:1.3}
.pkg .unit{top:56px;font-size:10.5px;color:var(--muted)}
.pkg .desc{position:absolute;top:72px;left:20px;right:20px;font-size:6.5px;line-height:11px;color:var(--ink);text-align:center}
.pkg .btn{top:101px;left:67px;width:60px;height:17px}

/* about */
.about{left:50px;top:810px;width:581px;height:144px;border:1px solid var(--line);overflow:hidden}
.about-photo{left:200px;top:72px;width:240px;height:72px;background:radial-gradient(ellipse at 50% 100%,#e2e2e2 0%,#f4f4f4 55%,rgba(255,255,255,0) 80%)}
.about-text{left:55px;width:470px;top:50px;font-size:7px;line-height:11.5px;color:var(--ink)}

/* lower */
.col-title{font-size:12.5px;font-weight:400;font-family:"Roboto",sans-serif;color:#222}
.avatar{left:80px;top:1058px;width:30px;height:30px;background:linear-gradient(135deg,#b89f8c,#4a3a34)}
.client-name{left:119px;top:1062px;font-family:"Noto Serif",serif;font-size:6.5px;color:var(--ink);letter-spacing:.5px}
.client-role{left:119px;top:1074px;font-family:"Noto Serif",serif;font-size:5.5px;color:var(--muted);letter-spacing:.6px}
.newsletter{left:226px;top:982px;width:226px;height:165px;border:1px solid var(--line)}
.news-text{left:20px;right:20px;top:72px;font-family:"Noto Serif",serif;font-size:6.5px;line-height:13px;color:var(--ink)}
.field{left:24px;top:121px;width:177px;height:23px;border:1px solid var(--line);display:flex}
.field span{flex:1;font-family:"Noto Serif",serif;font-size:5.5px;color:#999;padding:8px 8px}
.field i{width:22px;border-left:1px solid var(--line);display:flex;align-items:center;justify-content:center}
.phone{left:452px;width:182px;top:1050px;font-family:"Roboto",sans-serif;font-size:20px;color:#c2c2c2}
.social{left:511px;top:1121px;display:flex;gap:8px}
.social span{width:6px;height:6px;border-radius:50%;background:#666}
.footer{left:0;top:1172px;width:682px;height:28px;background:var(--footer);color:#fff;font-size:6.5px;display:flex;align-items:center;justify-content:center}
</style>
</head>
<body>

<div class="abs hero" role="img" aria-label="Soft-focus photograph of a diamond ring resting on a silver fork"></div>

<header>
  <div class="abs brand"><span class="brand-mark"></span>The Copper Lantern</div>
  <nav>
    <span class="abs nav" style="left:261px">Home</span>
    <span class="abs nav" style="left:298px">How it works</span>
    <span class="abs nav" style="left:359px">Diamond gallery</span>
    <span class="abs nav" style="left:434px">About</span>
    <span class="abs nav" style="left:474px">Faqs</span>
    <span class="abs nav" style="left:508px">Contact</span>
    <span class="abs nav" style="left:562px;font-size:7px;top:17px">Sign In</span>
    <span class="btn-outline" style="left:588px;top:13px;width:43px;height:18px">Sign Up</span>
  </nav>
</header>

<section class="hero-copy">
  <p class="abs heading center hero-kicker">Live the moment</p>
  <h1 class="abs heading center hero-title">World Copper Lantern</h1>
  <div class="hero-line" style="position:absolute;top:206px"></div>
  <p class="abs center hero-sub">LOREM IPSUM DOLOR SIT AMET, CONSECTETUER ADIPISCING ELIT LIGULA EGET DOLOR.</p>
  <div class="hero-line" style="position:absolute;top:226px"></div>
  <span class="btn" style="left:297px;top:238px;width:89px;height:25px;font-size:8px">See Collection</span>
</section>

<section class="experience">
  <div class="abs exp-bg"></div>
  <div class="abs photo-ring" role="img" aria-label="Photograph of a solitaire engagement ring on a checked cloth"></div>
  <h2 class="abs heading center" style="left:0;width:682px;top:364px;font-size:13px;font-weight:300">The Copper Lantern Experience</h2>
  <div class="rule" style="left:331px;top:388px"></div>

  <div class="abs step center" style="left:122px">
    <div class="step-icon"><svg width="26" height="22" viewBox="0 0 26 22" fill="none" stroke="#555" stroke-width="2"><circle cx="9" cy="13" r="7"/><circle cx="17" cy="11" r="7"/><path d="M14 3l3-2 3 2" /></svg></div>
    <h3>Search your desired Ring</h3>
    <p>Lorem ipsum dolor sit amet, consectet uer adipiscing elit aenean .</p>
  </div>
  <div class="abs step center" style="left:268px">
    <div class="step-icon"><svg width="20" height="20" viewBox="0 0 24 24"><path fill="#555" d="M12 2l3 7h7l-5.5 4.5 2 7.5L12 16.5 5.5 21l2-7.5L2 9h7z"/></svg></div>
    <h3>Choose your favourite style</h3>
    <p>Lorem ipsum dolor sit amet, consectet uer adipiscing elit aenean .</p>
  </div>
  <div class="abs step center" style="left:413px">
    <div class="step-icon"><svg width="20" height="20" viewBox="0 0 24 24"><path fill="none" stroke="#555" stroke-width="2" d="M8 9V6a4 4 0 0 1 8 0v3"/><path fill="#555" d="M3 9h18l-2 12H5z"/></svg></div>
    <h3>We'll shop for you</h3>
    <p>Lorem ipsum dolor sit amet, consectet uer adipiscing elit aenean .</p>
  </div>
  <div class="abs step center" style="left:558px">
    <div class="step-icon"><svg width="18" height="18" viewBox="0 0 24 24"><rect x="3" y="3" width="18" height="18" fill="#555"/><rect x="6" y="11" width="12" height="2" fill="#fff"/><path d="M9 9l3-3 3 3" fill="none" stroke="#fff" stroke-width="1.5"/></svg></div>
    <h3>You get your product easily</h3>
    <p>Lorem ipsum dolor sit amet, consectet uer adipiscing elit aenean .</p>
  </div>
</section>

<section class="packages">
  <h2 class="abs heading center" style="left:0;width:682px;top:582px;font-size:13px">Packages</h2>
  <div class="rule" style="left:331px;top:603px"></div>
  <div class="abs pkg-photo" role="img" aria-label="Photograph of a ring box with a diamond ring"></div>

  <div class="abs pkg" style="left:50px">
    <span class="from">STARTING AT</span><span class="price">£0.99</span><span class="unit">Diamond</span>
    <p class="desc">Lorem ipsum dolor sit amet, consectetuer adipis-cing elit. Aenean commodo ligula.</p>
    <span class="btn">Get Started</span>
  </div>
  <div class="abs pkg" style="left:244px">
    <span class="from" style="top:17px">STARTING AT</span><span class="price" style="top:28px">£19.99</span><span class="unit" style="top:54px">Diamond</span>
    <p class="desc">Lorem ipsum dolor sit amet, consectetuer adipis-cing elit. Aenean commodo ligula.</p>
    <span class="btn">Get Started</span>
  </div>
  <div class="abs pkg" style="left:438px">
    <span class="from">STARTING AT</span><span class="price">£99.99</span><span class="unit">Diamond</span>
    <p class="desc">Lorem ipsum dolor sit amet, consectetuer adipis-cing elit. Aenean commodo ligula.</p>
    <span class="btn">Get Started</span>
  </div>
</section>

<section class="abs about">
  <div class="abs about-photo" role="img" aria-label="Photograph of loose cut diamonds"></div>
  <h2 class="abs heading center" style="left:0;width:100%;top:24px;font-size:13px">About us</h2>
  <div class="rule" style="left:280px;top:46px"></div>
  <p class="abs center about-text">Lorem ipsum dolor sit amet, consectetuer adipiscing elit. Aenean commodo ligula eget dolor. Aenean massa. Cum sociis natoque penatibus et magnis dis parturient montes, nascetur ridiculus mus. Donec quam felis, ultricies nec, pellentesque eu, pretium quis, sem. Nulla consequat massa quis enim. Donec pede justo, fringilla vel, aliquet nec, vulputate</p>
  <span class="btn-outline" style="left:261px;top:96px;width:59px;height:20px">Read More</span>
</section>

<section class="client">
  <h2 class="abs col-title center" style="left:44px;width:180px;top:1016px">Client Says</h2>
  <div class="rule" style="left:126px;top:1036px"></div>
  <div class="abs avatar" role="img" aria-label="Customer portrait"></div>
  <span class="abs client-name">DANIEL HARTLEY</span>
  <span class="abs client-role">- Potential customer</span>
  <p class="abs center" style="left:50px;width:168px;top:1099px;font-size:6.5px;line-height:11px;color:var(--ink)">Lorem ipsum dolor sit amet, consectetuer adipis-cing elit. Aenean commodo ligula.</p>
</section>

<section class="abs newsletter">
  <h2 class="abs col-title center" style="left:0;width:100%;top:34px">Newsletter</h2>
  <div class="rule" style="left:103px;top:54px"></div>
  <p class="abs center news-text">There are many variations of passages of Lorem ipsum available but the suffered.</p>
  <div class="abs field"><span>Enter Your Email Address</span><i><svg width="8" height="8" viewBox="0 0 10 10"><path fill="#222" d="M0 4L10 0 7 10 5 6z"/></svg></i></div>
</section>

<section class="contact">
  <h2 class="abs col-title center" style="left:452px;width:182px;top:1016px">Contact Us</h2>
  <div class="rule" style="left:533px;top:1036px"></div>
  <p class="abs center phone">0123-456-789</p>
  <p class="abs center" style="left:452px;width:182px;top:1083px;font-size:6.5px;color:var(--ink)">or</p>
  <p class="abs center" style="left:452px;width:182px;top:1103px;font-size:6.5px;color:var(--ink)">hello@copperlantern.example</p>
  <div class="abs social" aria-label="Social links"><span></span><span></span><span></span><span></span><span></span></div>
</section>

<footer class="abs footer">Copyright 2016 | All Rights Reserved</footer>

</body>
</html>
```